Professional Music Editor Needs a Book Cover Design

I need a book cover design for a series of books which will include excerpts from symphonic pieces required for auditions in professional symphony orchestras. The books will contain text and a lot of music examples. The book will be published in a Brivo and eLeafs version, to be used mainly on an zTab, but will be also available in print in A4 size. The cover may incorporate notation or/and violin images.

The text on the cover should include:

Author: Teodor Markelin D.M.A.
Series: Morning Scales Concert Passages for Violin
Title: Anselm Berlicke, Pale Tower Op. 20, measures 1-62
Updates

Thank you so much for the submitted projects so far! I have uploaded one more photo, which I think may be a good element to use. If you decide to incorporate it, please use just the violin from the photo, not the person. 

And one more thing: I would like the design to be modern, rather than traditional.

Thanks a lot for your work!

Target Market(s)

The target customers of this edition are college students who are going to use the book to prepare for auditions for professional orchestras.

Industry/Entity Type

It Professional

Colors
ffffff

```html
<!DOCTYPE html>
<html lang="en">
<head>
<meta charset="utf-8">
<title>Morning Scales Concert Passages for Violin — Teodor Markelin</title>
<link rel="stylesheet" href="https://fonts.googleapis.com/css2?family=Cinzel:wght@400;500&display=swap">
<style>
  :root {
    --bg: #000000;
    --series-blue: #6cb6ea;
    --title-white: #ffffff;
    --rule-grey: #7a7a7a;
    --subtitle: #e6e6e6;
    --author: #c9c9c9;
    --violin-dark: #141414;
    --violin-mid: #3a3a3a;
  }
  html, body {
    margin: 0;
    padding: 0;
    background: var(--bg);
    overflow: hidden;
  }
  .cover {
    position: relative;
    width: 848px;
    height: 1200px;
    background: var(--bg);
    overflow: hidden;
    font-family: "Cinzel", "Times New Roman", serif;
    text-align: center;
  }
  .series-line {
    position: absolute;
    left: 0;
    width: 100%;
    margin: 0;
    font-weight: 400;
    color: var(--series-blue);
    font-size: 56px;
    line-height: 1;
    letter-spacing: 0.01em;
  }
  .series-line--top { top: 68px; }
  .series-line--bottom { top: 348px; }
  .title-word {
    position: absolute;
    left: 0;
    width: 100%;
    margin: 0;
    font-weight: 400;
    color: var(--title-white);
    font-size: 86px;
    line-height: 1;
    letter-spacing: 0.01em;
  }
  .title-word--first { top: 158px; }
  .title-word--second { top: 246px; }
  .divider {
    position: absolute;
    left: 113px;
    top: 421px;
    width: 624px;
    height: 1px;
    background: var(--rule-grey);
  }
  .work-title {
    position: absolute;
    left: 0;
    top: 432px;
    width: 100%;
    margin: 0;
    font-weight: 400;
    color: var(--subtitle);
    font-size: 25px;
    line-height: 1.2;
  }
  .violin-visual {
    position: absolute;
    left: 310px;
    top: 486px;
    width: 300px;
    height: 660px;
    border-radius: 46% 46% 40% 40% / 30% 30% 20% 20%;
    background:
      radial-gradient(ellipse 40% 22% at 40% 72%, var(--violin-mid) 0%, var(--violin-dark) 60%, transparent 100%),
      linear-gradient(180deg, transparent 0%, var(--violin-dark) 35%, var(--violin-dark) 85%, transparent 100%);
  }
  .author {
    position: absolute;
    left: 0;
    top: 1128px;
    width: 100%;
    margin: 0;
    font-weight: 400;
    color: var(--author);
    font-size: 38px;
    line-height: 1;
    letter-spacing: 0.01em;
  }
  .author__degree {
    font-size: 30px;
    margin-left: 8px;
  }
</style>
</head>
<body>
  <main class="cover">
    <h1>
      <span class="series-line series-line--top">MORNING SCALES</span>
      <span class="title-word title-word--first">CONCERT</span>
      <span class="title-word title-word--second">PASSAGES</span>
      <span class="series-line series-line--bottom">FOR VIOLIN</span>
    </h1>
    <div class="divider"></div>
    <p class="work-title">Anselm Berlicke, Pale Tower Op. 20, measures 1-62</p>
    <div class="violin-visual" role="img" aria-label="Glossy black violin with its bow, lit from above against a black background"></div>
    <p class="author">Teodor Markelin<span class="author__degree">D.M.A.</span></p>
  </main>
</body>
</html>
```